Event branding Sales presentation PowerPoint template required

We are looking to freshen up & step up the professional quality of our powerpoint presentation template. I am looking for a professional designer with good creative background to design a new template for our presentations to new clients and for bespoke projects.
We have attached our current PPP as well as an elevator pitch which has most of the information we would like on the template

We have 3 main parts of our business which are:
- Event Branding
- Fan Engagements
- Set builds / Theming

Target Market(s)

Event organisers and sporting fedrations

Industry/Entity Type

Events

Requirements
Must have
• Ability for easy editing. Strong visual representation
Nice to have
• Information pages as well as look-book pages
Should not have
• Overcrowded graphics / arty graphics

```html
<!DOCTYPE html>
<html lang="en">
<head>
<meta charset="utf-8">
<title>Arclight Events – Event Branding &amp; Fan Engagement Deck</title>
<link href="https://fonts.googleapis.com/css2?family=Montserrat:wght@500;700;800;900&family=Lato:wght@400;700&display=swap" rel="stylesheet">
<style>
:root{
  --canvas:#d3d3d3;
  --ink:#0b0b0b;
  --gold:#c6a664;
  --gold-soft:#d8bf86;
  --cream:#f5f1e6;
  --white:#ffffff;
  --body:#2a2a2a;
  --muted:#9a9a9a;
}
*{box-sizing:border-box;margin:0;padding:0}
html,body{width:678px;height:1200px;overflow:hidden;background:var(--canvas)}
body{position:relative;font-family:"Lato",sans-serif;color:var(--body)}
.slide{position:absolute;width:305px;height:172px;overflow:hidden}
.slide.dark{background:var(--ink);color:var(--white)}
.slide.light{background:var(--white)}
.slide.cream{background:var(--cream)}
.col-l{left:24px}.col-r{left:348px}
.r1{top:42px}.r2{top:231px}.r3{top:420px}.r4{top:607px}.r5{top:792px}.r6{top:982px}
.abs{position:absolute}
.photo{position:absolute}
.heading{font-family:"Montserrat",sans-serif;font-weight:900;letter-spacing:.2px;text-transform:uppercase}
.gold{color:var(--gold)}
.tiny{font-size:3.6px;line-height:1.35;text-align:center}
.small{font-size:4.2px;line-height:1.4}
/* footer */
.footer{position:absolute;left:10px;right:8px;bottom:8px;height:12px}
.footer .brand{position:absolute;left:0;bottom:0;font-family:"Montserrat",sans-serif;font-weight:700;font-size:3.6px;letter-spacing:.6px;color:var(--gold)}
.footer .mark{position:absolute;left:4px;bottom:5px;width:8px;height:8px;border:.6px solid var(--gold);border-radius:50%}
.footer .rule{position:absolute;left:40px;right:4px;bottom:3px;height:.6px;background:var(--gold)}
.footer .dot{position:absolute;right:0;bottom:1px;width:5px;height:5px;border-radius:50%;background:var(--gold)}
/* cards */
.card{position:absolute;top:42px;width:82px;height:100px;background:var(--white);color:var(--body)}
.card .ring{position:absolute;left:50%;top:-16px;width:50px;height:50px;margin-left:-25px;border-radius:50%;border:2px solid var(--gold);overflow:hidden}
.card .ring .photo{inset:0}
.card .title{position:absolute;top:42px;left:0;right:0;text-align:center;font-size:5.4px;color:var(--gold)}
.card .tiny{position:absolute;top:54px;left:6px;right:6px;color:#444}
/* lookbook */
.seal{position:absolute;width:60px;height:60px;border-radius:50%;background:var(--gold);display:flex;align-items:center;justify-content:center;text-align:center;color:var(--ink);font-family:"Montserrat",sans-serif;font-weight:900;line-height:1.05}
.bullets{position:absolute;list-style:none;font-family:"Montserrat",sans-serif;font-weight:500;font-size:5px;line-height:1.3;color:var(--white)}
.bullets li::before{content:"•";color:var(--white);margin-right:5px}
/* contents */
.step{position:absolute;top:30px;width:44px;text-align:center}
.step .num{width:17px;height:17px;margin:0 auto;border-radius:50%;background:var(--ink);border:1.4px solid var(--gold);color:var(--white);font-family:"Montserrat",sans-serif;font-weight:800;font-size:8px;line-height:14.5px}
.step .lbl{margin-top:7px;font-family:"Montserrat",sans-serif;font-weight:800;font-size:3.8px;color:var(--gold);line-height:1.15;height:14px}
.step .tiny{margin-top:3px;color:#333;font-size:3px}
/* turnkey */
.node{position:absolute;width:50px;text-align:center;font-family:"Montserrat",sans-serif;font-weight:800;font-size:3.6px;color:var(--gold);line-height:1.1}
.node .ico{width:16px;height:16px;margin:0 auto;border-radius:50%;border:1px solid var(--gold)}
/* fan flow */
.chev{position:absolute;top:120px;height:10px;width:52px;background:var(--white);color:var(--gold);font-family:"Montserrat",sans-serif;font-weight:900;font-size:5px;line-height:10px;padding-left:10px;clip-path:polygon(0 0,90% 0,100% 50%,90% 100%,0 100%)}
.flow-photo{position:absolute;top:28px;width:44px;height:44px;border-radius:50%;overflow:hidden}
.flow-text{position:absolute;top:134px;width:52px;font-size:2.8px;line-height:1.35;color:#ddd}
</style>
</head>
<body>

<!-- 1 Cover -->
<section class="slide light col-l r1">
  <div class="photo" style="left:0;top:0;width:101px;height:72px;background:linear-gradient(135deg,#6e87a6,#3d4a66 60%,#8a9bb3)" role="img" aria-label="Stadium exterior with large branded wrap"></div>
  <div class="photo" style="left:0;top:72px;width:101px;height:73px;background:linear-gradient(160deg,#b7c9d8,#7fae4a 55%,#4d7d2f)" role="img" aria-label="Giant 3D hashtag letters on grass"></div>
  <div class="abs" style="left:101px;top:0;width:102px;height:145px;background:var(--ink)">
    <div class="abs" style="left:12px;top:-6px;width:78px;height:78px;border:1px solid var(--gold);border-radius:50%"></div>
    <div class="abs" style="left:42px;top:12px;width:18px;height:18px;border:.8px solid var(--gold);border-radius:50%"></div>
    <div class="abs heading" style="left:0;right:0;top:43px;text-align:center;font-weight:500;font-size:5.4px;letter-spacing:1.4px;color:var(--gold)">Arclight Events</div>
    <div class="abs" style="left:10px;top:103px;font-family:'Montserrat',sans-serif;font-weight:500;font-size:10px;line-height:.95;color:var(--white)">NUMBER<br>CHOICE</div>
    <div class="abs" style="left:70px;top:103px;width:20px;height:20px;border-radius:50%;background:var(--gold);color:var(--ink);font-family:'Montserrat',sans-serif;font-weight:700;font-size:8px;line-height:20px;text-align:center">#1</div>
  </div>
  <div class="photo" style="left:203px;top:0;width:102px;height:72px;background:radial-gradient(circle at 50% 40%,#8ea4d8,#34405e 70%)" role="img" aria-label="Venue ceiling with suspended lighting rings"></div>
  <div class="photo" style="left:203px;top:72px;width:102px;height:73px;background:linear-gradient(180deg,#6d6f8a,#b04b8e 50%,#3f7a3a)" role="img" aria-label="Stadium crowd with fan flags"></div>
  <div class="abs heading" style="left:0;right:0;top:151px;text-align:center;font-size:10.6px;color:var(--gold);letter-spacing:.1px">Event Branding &amp; Fan Engagement</div>
</section>

<!-- 2 Contents -->
<section class="slide cream col-r r1">
  <div class="abs heading gold" style="left:0;right:0;top:9px;text-align:center;font-size:10px">Contents</div>
  <div class="abs" style="left:30px;right:30px;top:38px;height:1px;background:var(--ink)"></div>
  <div class="step" style="left:13px"><div class="num">1</div><div class="lbl">ABOUT US</div><p class="tiny">A brief overview of Arclight Events</p></div>
  <div class="step" style="left:60px"><div class="num">2</div><div class="lbl">UNIQUE PERSPECTIVE</div><p class="tiny">What makes us different and a good supply partner to Orbis</p></div>
  <div class="step" style="left:107px"><div class="num">3</div><div class="lbl">TURNKEY SOLUTIONS</div><p class="tiny">From initial concept or event plan, our team can manage all your branding and fan engagement needs up to completion and beyond.</p></div>
  <div class="step" style="left:154px"><div class="num">4</div><div class="lbl">OUR SERVICES</div><p class="tiny">A brief list of our core services and the elements we specialise in</p></div>
  <div class="step" style="left:201px"><div class="num">5</div><div class="lbl">PROJECT EXAMPLES</div><p class="tiny">A few select examples of various projects we have been involved in.</p></div>
  <div class="step" style="left:248px"><div class="num">6</div><div class="lbl">WHY ARCLIGHT EVENTS</div><p class="tiny">Discover how we can launch your fan engagement project and branding above the standard.</p></div>
  <div class="footer"><span class="mark"></span><span class="brand">ARCLIGHT EVENTS</span><span class="rule"></span><span class="dot"></span></div>
</section>

<!-- 3 About -->
<section class="slide light col-l r2">
  <div class="photo" style="left:235px;top:0;width:70px;height:132px;background:linear-gradient(180deg,#aab7c9,#6f7d8f 50%,#c9c2b3)" role="img" aria-label="Person in a venue concourse under lighting installation"></div>
  <div class="abs heading" style="left:150px;top:30px;width:90px;height:16px;background:var(--gold);color:var(--ink);font-size:9.4px;line-height:16px;text-align:center">About Us</div>
  <div class="abs" style="left:14px;top:52px;font-size:6.2px;color:var(--gold);font-weight:700">Welcome!</div>
  <div class="abs small" style="left:14px;top:64px;width:214px;font-size:3.5px;text-align:justify;color:#333">
    <p><b>Arclight Events</b> boasts an international presence with established partners and relationships globally. We punch well above our weight in the capability of our services. With a wealth of experience with venues and events across the globe developing temporary and permanent branding, themes, set builds, integrated rigging and signage, your branding and fan engagement is in good hands with a partner who understands the changing demand for flexibility and quality.</p>
    <p style="margin-top:3px">The Arclight Events team has worked on iconic venues around the world including stadiums, Olympic parks, exhibition centres, dedicated event venues, museums and art galleries.</p>
    <p style="margin-top:3px">The following will give you an idea about how we can work with Orbis Basketball to take a step forward in your fan engagement and branding, and we can also offer partnerships to sell media space at your venues.</p>
  </div>
  <div class="abs" style="left:14px;top:122px;width:209px;height:11px;background:var(--ink);color:var(--gold-soft);font-size:6px;font-weight:700;line-height:11px;padding-left:5px">Pushing the boundaries, delivering the <span style="color:var(--white)">highest quality.</span></div>
  <div class="footer"><span class="mark"></span><span class="brand">ARCLIGHT EVENTS</span><span class="rule"></span><span class="dot"></span></div>
</section>

<!-- 4 Unique perspectives -->
<section class="slide dark col-r r2">
  <div class="abs" style="left:95px;right:0;top:42px;height:86px;background:var(--white)"></div>
  <div class="abs" style="left:12px;top:44px;width:90px;height:90px;border-radius:50%;border:1.4px solid var(--gold);overflow:hidden">
    <div class="photo" style="inset:0;background:radial-gradient(circle,#e07a3a,#8a2f3f 45%,#1d1433 80%)" role="img" aria-label="Performer on stilts in front of an illuminated observation wheel"></div>
  </div>
  <div class="abs heading" style="left:137px;top:28px;font-size:10.4px;color:var(--white)">Unique <span class="gold">Perspectives</span></div>
  <div class="abs" style="left:137px;top:56px;font-size:5.8px;color:var(--gold)">Beyond Standard Branding</div>
  <div class="abs small" style="left:137px;top:66px;width:160px;font-size:3.5px;color:#333;text-align:justify">
    <p>One of our strongest attributes is that our team comes from various industries originally and developed our service around creative delivery. With industries including film, rigging, outdoor advertising and set builds, we are able to provide unique additions to your branding and fan engagement to really stand out.</p>
    <p style="margin-top:3px">This could be a simple 2D image extension beyond a bridge edge or a bespoke giant immersive basketball.</p>
    <p style="margin-top:3px">We build our props in-house, print and install ourselves with additional global partners where needed.</p>
  </div>
  <div class="footer"><span class="mark"></span><span class="brand">ARCLIGHT EVENTS</span><span class="rule"></span><span class="dot"></span></div>
</section>

<!-- 5 Turnkey -->
<section class="slide dark col-l r3">
  <div class="abs heading" style="left:0;right:0;top:14px;text-align:center;font-size:10.6px">Turnkey <span class="gold">Solutions</span></div>
  <svg class="abs" style="left:0;top:0" width="305" height="172" aria-hidden="true">
    <g stroke="#c6a664" stroke-width=".8" fill="none">
      <line x1="34" y1="82" x2="278" y2="82"/>
      <line x1="34" y1="74" x2="34" y2="82"/><line x1="118" y1="74" x2="118" y2="82"/>
      <line x1="198" y1="74" x2="198" y2="82"/><line x1="278" y1="74" x2="278" y2="82"/>
      <line x1="78" y1="82" x2="78" y2="92"/><line x1="158" y1="82" x2="158" y2="92"/><line x1="238" y1="82" x2="238" y2="92"/>
    </g>
  </svg>
  <div class="node" style="left:9px;top:40px">CONCEPT<div class="ico" style="margin-top:4px"></div></div>
  <div class="node" style="left:93px;top:40px">DESIGN<div class="ico" style="margin-top:4px"></div></div>
  <div class="node" style="left:173px;top:36px">INTERNATIONAL LOGISTICS<div class="ico" style="margin-top:4px"></div></div>
  <div class="node" style="left:253px;top:36px">FULL PROJECT MANAGEMENT<div class="ico" style="margin-top:4px"></div></div>
  <div class="node" style="left:53px;top:92px"><div class="ico" style="margin-bottom:3px"></div>SURVEY &amp; PROPOSAL</div>
  <div class="node" style="left:133px;top:92px"><div class="ico" style="margin-bottom:3px"></div>BUILD/ PRINT</div>
  <div class="node" style="left:213px;top:92px"><div class="ico" style="margin-bottom:3px"></div>INSTALLATION &amp; RIGGING</div>
  <p class="abs tiny" style="left:0;right:0;top:136px;color:#ddd;font-size:3.6px">Our team can assist through every step of your event.<br>Providing the highest standards of delivery our professionals will guide you through each technical milestone.</p>
  <div class="abs" style="left:0;right:0;top:148px;text-align:center;font-size:6.4px;font-weight:700">Reaching your goals, together.</div>
  <div class="footer"><span class="mark"></span><span class="brand">ARCLIGHT EVENTS</span><span class="rule"></span><span class="dot"></span></div>
</section>

<!-- 6 Services A -->
<section class="slide dark col-r r3">
  <div class="abs heading" style="left:0;right:0;top:8px;text-align:center;font-size:10.6px">Our <span class="gold">Services</span></div>
  <div class="card" style="left:14px"><div class="ring"><div class="photo" style="background:radial-gradient(circle,#e44a2a,#5b1a4a 50%,#140b22)" role="img" aria-label="Illuminated hexagon stage tunnel"></div></div><div class="title heading">Branding</div><p class="tiny">We have a sustainable approach to branding and can provide interchangeable graphic solutions to your venue and source sustainable materials across the board. We produce, fit and remove a very wide range of graphics.</p></div>
  <div class="card" style="left:112px"><div class="ring"><div class="photo" style="background:linear-gradient(160deg,#b7c9d8,#7fae4a 55%,#d45a4a)" role="img" aria-label="Giant 3D hashtag letters"></div></div><div class="title heading">Fan Engagement</div><p class="tiny">Fan engagement is a huge part of branding. Make your event fan zones an unforgettable social media moment. We can design, build, deliver and install your special creation.</p></div>
  <div class="card" style="left:210px"><div class="ring"><div class="photo" style="background:linear-gradient(135deg,#6a6e78,#3c4048 60%,#5e7d4a)" role="img" aria-label="Building wrap with a bespoke car prop"></div></div><div class="title heading">Bespoke Builds</div><p class="tiny">We can design and build anything from large 3D letters to full set and prop builds. We can offer bespoke signage and unique blends of graphics and 3D elements to increase the visual experience of your event.</p></div>
  <div class="footer"><span class="mark"></span><span class="brand">ARCLIGHT EVENTS</span><span class="rule"></span><span class="dot"></span></div>
</section>

<!-- 7 Services B -->
<section class="slide dark col-l r4">
  <div class="abs heading" style="left:0;right:0;top:8px;text-align:center;font-size:10.6px">Our <span class="gold">Services</span></div>
  <div class="card" style="left:14px"><div class="ring"><div class="photo" style="background:linear-gradient(180deg,#6e8fc0,#dfe4ea 55%,#7a8088)" role="img" aria-label="Stadium stand wrapped in fabric"></div></div><div class="title heading">Rigging</div><p class="tiny">From banner drops off a stadium roof edge to zip lines or 3D suspended replicas, our experienced team of riggers will find a solution to any challenge.</p></div>
  <div class="card" style="left:112px"><div class="ring"><div class="photo" style="background:linear-gradient(180deg,#5a7fb8,#2a3a7a 50%,#7a5a8a)" role="img" aria-label="Large format banner over a stadium crowd"></div></div><div class="title heading">Large Format</div><p class="tiny">We can bring any of your big ideas to life, and then install them from the roof tops. No print is too large and with our certified rope access crew we can make your fan engagement plans come to life.</p></div>
  <div class="card" style="left:210px"><div class="ring"><div class="photo" style="background:radial-gradient(circle,#b8c6e8,#4b5a86 65%)" role="img" aria-label="Venue ceiling with integrated lighting"></div></div><div class="title heading" style="top:39px;line-height:1">Technology Integrations</div><p class="tiny" style="top:56px">Need LED screens integrated with motion, drone performances, robots pouring beer, VR experiences? Between our team and our partners your imagination is our limit.</p></div>
  <div class="footer"><span class="mark"></span><span class="brand">ARCLIGHT EVENTS</span><span class="rule"></span><span class="dot"></span></div>
</section>

<!-- 8 Branding lookbook -->
<section class="slide dark col-r r4">
  <div class="photo" style="left:0;top:0;width:101px;height:57px;background:radial-gradient(circle,#e44a2a,#4a1a3a 55%,#120a1a)" role="img" aria-label="Hexagon stage tunnel and event set"></div>
  <div class="photo" style="left:0;top:57px;width:101px;height:45px;background:linear-gradient(135deg,#2b2b2b,#8a1f1f 50%,#d0d0d0)" role="img" aria-label="Motorsport pit lane branding"></div>
  <div class="photo" style="left:0;top:102px;width:101px;height:70px;background:linear-gradient(180deg,#9fb6cf,#5d7fa8 50%,#3ea0c8)" role="img" aria-label="Branded trackside grandstands"></div>
  <div class="seal" style="left:112px;top:15px;width:80px;height:80px;font-size:9.6px">BRANDING</div>
  <ul class="bullets" style="left:122px;top:108px"><li>SCOPING</li><li>DESIGN</li><li>PRINT</li><li>INSTALLATION</li></ul>
  <div class="photo" style="left:203px;top:0;width:102px;height:85px;background:linear-gradient(180deg,#6e8fc0,#e5e8ec 55%,#8a9096)" role="img" aria-label="Stadium stand wrapped in white fabric"></div>
  <div class="photo" style="left:203px;top:85px;width:102px;height:87px;background:linear-gradient(180deg,#5a7fb8,#1f2f6e 55%,#6a4a7a)" role="img" aria-label="Giant banner above stadium crowd"></div>
</section>

<!-- 9 Fan engagement lookbook -->
<section class="slide dark col-l r5">
  <div class="photo" style="left:0;top:0;width:101px;height:87px;background:linear-gradient(160deg,#c83a2a,#e8b23a 50%,#3a7ab8)" role="img" aria-label="Festive carousel at a fan zone"></div>
  <div class="photo" style="left:0;top:87px;width:101px;height:85px;background:linear-gradient(160deg,#b7c9d8,#7fae4a 55%,#d45a4a)" role="img" aria-label="Giant 3D hashtag letters on grass"></div>
  <div class="abs" style="left:101px;top:0;width:102px;height:172px;background:var(--ink)"></div>
  <div class="seal" style="left:112px;top:10px;width:80px;height:80px;font-size:7.4px;flex-direction:column"><span style="font-size:13px">FAN</span>ENGAGEMENT</div>
  <ul class="bullets" style="left:122px;top:104px"><li>BUILDS</li><li>PRINT</li><li>SIGNAGE</li><li>THEMING</li><li>BANNERS</li></ul>
  <div class="photo" style="left:203px;top:0;width:102px;height:87px;background:linear-gradient(180deg,#8a8f98,#3b3f58 55%,#6a5ab0)" role="img" aria-label="Covered arena with lighting rig"></div>
  <div class="photo" style="left:203px;top:87px;width:102px;height:85px;background:linear-gradient(180deg,#b8c8d8,#7a8aa0 45%,#4e7a3a)" role="img" aria-label="Outdoor fan zone with big screen"></div>
</section>

<!-- 10 Fan engagement case -->
<section class="slide dark col-r r5">
  <div class="abs heading gold" style="left:0;right:0;top:10px;text-align:center;font-size:10.6px">Fan Engagement</div>
  <div class="flow-photo" style="left:19px;background:linear-gradient(180deg,#eef2f6,#3b5ba8 55%,#3d7a3a)" role="img" aria-label="Stadium bowl view"></div>
  <div class="flow-photo" style="left:90px;background:linear-gradient(180deg,#d8e0ea,#2a4a9a 60%)" role="img" aria-label="Stadium stands"></div>
  <div class="flow-photo" style="left:161px;background:linear-gradient(180deg,#e8ecf0,#4a6aa8 50%,#4a8a3a)" role="img" aria-label="Rigging in stadium roof"></div>
  <div class="flow-photo" style="left:232px;background:linear-gradient(180deg,#7a8ab8,#2a3a6a 60%)" role="img" aria-label="Giant banner revealed over stand"></div>
  <div class="chev" style="left:12px">CONCEPT</div>
  <div class="chev" style="left:83px">DESIGN</div>
  <div class="chev" style="left:154px">SOLUTION</div>
  <div class="chev" style="left:225px">SUCCESS</div>
  <p class="flow-text" style="left:12px">RVFC asked our team to design, print, rig and activate a giant reveal of their new brand. This was to drop as the players entered the pitch and retract at the start of the match.</p>
  <p class="flow-text" style="left:83px">The stadium posed a unique challenge. We designed a bespoke dual pulley system with 9 independent operational systems to ensure its safety and smooth operation.</p>
  <p class="flow-text" style="left:154px">Our high-access riggers had to scale the internal structure and set up a bespoke rig that was safe and fully operational. This had to be removable at the match start.</p>
  <p class="flow-text" style="left:225px">The impact was amazing! RVFC not only won the match but went on the Continental Cup finals. They won every match with this rig.</p>
  <div class="footer" style="bottom:4px"><span class="mark"></span><span class="brand">ARCLIGHT EVENTS</span><span class="rule"></span><span class="dot"></span></div>
</section>

<!-- 11 Bespoke builds lookbook -->
<section class="slide dark col-l r6">
  <div class="photo" style="left:0;top:0;width:101px;height:118px;background:linear-gradient(180deg,#6a6e78,#3c4048 50%,#8a96b8)" role="img" aria-label="Building wrap with car prop and carriage interior"></div>
  <div class="photo" style="left:0;top:118px;width:101px;height:54px;background:linear-gradient(135deg,#c82a2a,#6a6e78 55%,#2a2a30)" role="img" aria-label="Replica train carriage"></div>
  <div class="seal" style="left:112px;top:10px;width:80px;height:80px;font-size:10px">BESPOKE<br>BUILDS</div>
  <ul class="bullets" style="left:118px;top:100px;font-size:4.8px"><li>GIANT LETTERS/</li><li style="list-style:none">&nbsp;&nbsp;&nbsp;LOGO</li><li>REPLICAS</li><li>TUNNELS/</li><li style="list-style:none">&nbsp;&nbsp;&nbsp;PLATFORMS</li><li>THEMING/</li><li style="list-style:none">&nbsp;&nbsp;&nbsp;SET BUILDS</li></ul>
  <div class="photo" style="left:203px;top:0;width:102px;height:57px;background:linear-gradient(180deg,#9aa6b4,#6a6058 60%)" role="img" aria-label="City street building facade"></div>
  <div class="photo" style="left:203px;top:57px;width:102px;height:55px;background:linear-gradient(135deg,#5a5a5e,#9a9aa0 50%,#3a3a3e)" role="img" aria-label="Aircraft fuselage replica build"></div>
  <div class="photo" style="left:203px;top:112px;width:102px;height:60px;background:radial-gradient(circle,#e44a2a,#3a6a9a 55%,#120a1a)" role="img" aria-label="Illuminated stage set build"></div>
</section>

<!-- 12 Installation -->
<section class="slide dark col-r r6">
  <div class="photo" style="left:4px;top:4px;width:97px;height:60px;background:linear-gradient(180deg,#dfe8f4,#6a8ab8 50%,#2a4a8a)" role="img" aria-label="Branded stadium roof edge"></div>
  <div class="abs heading gold" style="left:4px;width:97px;top:74px;text-align:center;font-size:7.4px;line-height:1.05">High Quality<br>Standards</div>
  <p class="abs small" style="left:12px;width:81px;top:96px;text-align:center;color:#ddd;font-size:4.1px">Our experienced teams will make sure all aspects of your project are completed safely and efficiently.</p>
  <div class="abs" style="left:4px;width:97px;top:122px;text-align:center;font-size:4.1px;color:var(--gold)">Design, builds and installation</div>
  <div class="abs" style="left:101px;top:0;width:102px;height:172px;background:linear-gradient(180deg,var(--white) 55%,#e6e6e6)"></div>
  <div class="seal" style="left:112px;top:24px;width:80px;height:80px;font-size:8.6px">INSTALLATION</div>
  <div class="abs" style="left:101px;width:102px;top:108px;text-align:center;font-family:'Montserrat',sans-serif;font-weight:500;font-size:5.6px;color:var(--ink);line-height:1.15">OUR PROFESSIONALS<br><span class="gold">ARE AT YOUR<br>DISPOSAL</span></div>
  <div class="photo" style="left:208px;top:4px;width:93px;height:60px;background:linear-gradient(180deg,#f2f4f6,#d8dde2 60%,#7a9a3a)" role="img" aria-label="Rope access technician working at height"></div>
  <div class="abs heading gold" style="left:203px;width:102px;top:74px;text-align:center;font-size:7.4px;line-height:1.05">Complex<br>Projects</div>
  <p class="abs small" style="left:212px;width:84px;top:100px;text-align:center;color:#ddd;font-size:4px">Our certified rope access crew will make sure your project goes off without a hitch. We pride ourselves on our safety culture. <span class="gold">All projects are managed by experienced teams.</span></p>
</section>

</body>
</html>
```